Business card design needed

Just need something dynamic and unique
For a local painting contractor

Industry/Entity Type

Painting

Contact Information for Business Card

Warren Pike
Painting Contactor
Interior & Exterior
New Work & Repaints
For an obligation free quote:
0437516082

```html
<!DOCTYPE html>
<html lang="en">
<head>
<meta charset="utf-8">
<title>Warren Pike – Painting Contractor Business Card</title>
<link href="https://fonts.googleapis.com/css2?family=Kaushan+Script&family=Open+Sans:ital,wght@0,400;0,600;0,700;1,600&display=swap" rel="stylesheet">
<style>
  :root {
    --paint-red: #c0161d;
    --deep-red: #9e1218;
    --paper-white: #ffffff;
    --ink-dark: #1f1f1f;
    --rule-dark: #5a0d10;
    --backdrop: #ecebe8;
    --roller-tone: #d9d4d2;
  }
  * { margin: 0; padding: 0; box-sizing: border-box; }
  html, body {
    width: 1200px;
    height: 868px;
    overflow: hidden;
    background: var(--backdrop);
  }
  .stage {
    position: relative;
    width: 1200px;
    height: 868px;
  }
  .card {
    position: absolute;
    width: 540px;
    height: 310px;
    border-radius: 12px;
    overflow: hidden;
    background: var(--paint-red);
    box-shadow: 0 6px 18px rgba(0,0,0,0.18);
  }
  .card-back { left: 40px; top: 279px; }
  .card-front { left: 620px; top: 279px; }
  .card svg { position: absolute; inset: 0; }
  .name {
    position: absolute;
    left: 62px;
    top: 30px;
    font-family: "Kaushan Script", cursive;
    font-size: 36px;
    color: var(--ink-dark);
    line-height: 1;
  }
  .role {
    position: absolute;
    left: 64px;
    top: 76px;
    font-family: "Open Sans", sans-serif;
    font-style: italic;
    font-weight: 600;
    font-size: 14px;
    color: var(--paint-red);
  }
  .services {
    position: absolute;
    left: 66px;
    top: 178px;
    font-family: "Open Sans", sans-serif;
    font-size: 15px;
    line-height: 22px;
    color: var(--paper-white);
    list-style: none;
  }
  .divider {
    position: absolute;
    left: 60px;
    top: 234px;
    width: 420px;
    height: 1px;
    background: var(--rule-dark);
  }
  .quote {
    position: absolute;
    left: 60px;
    top: 246px;
    font-family: "Open Sans", sans-serif;
    font-size: 15px;
    color: var(--paper-white);
  }
  .quote strong { font-weight: 700; letter-spacing: 0.5px; }
</style>
</head>
<body>
<main class="stage">

  <section class="card card-back" aria-label="Card back">
    <svg width="540" height="310" viewBox="0 0 540 310">
      <rect class="base" width="540" height="310" fill="var(--paint-red)"/>
      <polygon class="painted-stroke" points="374,0 540,0 540,310 250,310 258,120 374,110" fill="var(--paper-white)"/>
      <polygon class="streak" points="135,40 140,40 60,310 54,310" fill="var(--paper-white)"/>
      <polygon class="streak" points="175,170 179,170 150,310 146,310" fill="var(--paper-white)"/>
      <polygon class="streak" points="232,0 235,0 222,70 219,70" fill="var(--paper-white)"/>
      <rect class="roller" x="262" y="95" width="110" height="160" rx="10" fill="var(--roller-tone)" role="img" aria-label="Paint roller illustration"/>
    </svg>
  </section>

  <section class="card card-front" aria-label="Card front">
    <svg width="540" height="310" viewBox="0 0 540 310">
      <rect class="base" width="540" height="310" fill="var(--paint-red)"/>
      <polygon class="painted-area" points="0,0 292,0 292,152 0,114" fill="var(--paper-white)"/>
      <polygon class="painted-patch" points="290,310 470,238 490,254 482,276 500,310" fill="var(--paper-white)"/>
      <rect class="roller" x="292" y="62" width="240" height="120" rx="10" fill="var(--deep-red)" role="img" aria-label="Paint roller illustration"/>
    </svg>
    <h1 class="name">Warren Pike</h1>
    <p class="role">Painting Contactor</p>
    <ul class="services">
      <li>Interior &amp; Exterior</li>
      <li>New Work &amp; Repaints</li>
    </ul>
    <div class="divider"></div>
    <p class="quote">For an obligation free quote: <strong>0437516082</strong></p>
  </section>

</main>
</body>
</html>
```